Reed & Vale NC grand opening (for BILLBOARD)

Advertising the grand opening of our cannabis/hemp shop in NC. We will sell all things hemp (flower, cartridges, disposables, edibles, creams, lotions, pet products etc...)

Requirements
Must have
• include, open starting Aug 1, but grand opening Aug 15th.
Nice to have
• Difference slogan ideas "Save some cash, buy our grass" "Find your perfect high at Reed & Vale cannabis store" "Experience Nature's Gift: Reed & Vale Cannabis Store"

```html
<!DOCTYPE html>
<html lang="en">
<head>
<meta charset="utf-8">
<title>Reed &amp; Vale Billboard</title>
<link href="https://fonts.googleapis.com/css2?family=Poppins:wght@500;600;700;800&display=swap" rel="stylesheet">
<style>
  :root {
    --backdrop: #cfcfcf;
    --board-dark: #0c0f10;
    --board-mid: #1a2022;
    --leaf-deep: #1f4a1e;
    --leaf-mid: #2f6a2a;
    --brand-green: #6cb33f;
    --banner-green: #69a83d;
    --ink-dark: #13210f;
    --white: #ffffff;
  }
  * { margin: 0; padding: 0; box-sizing: border-box; }
  html, body {
    width: 1200px;
    height: 456px;
    overflow: hidden;
    background: var(--backdrop);
    font-family: "Poppins", sans-serif;
  }
  .billboard {
    position: absolute;
    left: 73px;
    top: 62px;
    width: 1054px;
    height: 309px;
    overflow: hidden;
    background: radial-gradient(ellipse at 72% 40%, var(--board-mid) 0%, var(--board-dark) 70%);
    box-shadow: 4px 6px 8px rgba(0,0,0,0.35);
  }
  .foliage { position: absolute; }
  .foliage--left {
    left: 0;
    top: 0;
    width: 560px;
    height: 309px;
    background:
      radial-gradient(ellipse 60% 45% at 40% 95%, var(--leaf-mid) 0%, rgba(31,74,30,0.6) 45%, transparent 75%),
      radial-gradient(ellipse 35% 30% at 22% 12%, rgba(31,74,30,0.55) 0%, transparent 80%);
  }
  .foliage--right {
    right: 0;
    bottom: 0;
    width: 330px;
    height: 150px;
    background: radial-gradient(ellipse 65% 70% at 75% 100%, rgba(47,106,42,0.55) 0%, rgba(31,74,30,0.25) 50%, transparent 80%);
  }
  .headline-banner {
    position: absolute;
    left: -4px;
    top: 65px;
    width: 564px;
    height: 178px;
    background: var(--banner-green);
    border: 2px solid var(--white);
    border-radius: 0 89px 89px 0;
    padding: 16px 0 0 45px;
  }
  .headline {
    color: var(--white);
    font-weight: 800;
    font-size: 54px;
    line-height: 52px;
    letter-spacing: 0.3px;
  }
  .subline {
    margin-top: 8px;
    color: var(--ink-dark);
    font-weight: 700;
    font-size: 27.5px;
    line-height: 32px;
    white-space: nowrap;
  }
  .brand {
    position: absolute;
    left: 620px;
    top: 108px;
    display: flex;
    align-items: center;
    gap: 14px;
  }
  .brand-dot {
    width: 22px;
    height: 22px;
    border-radius: 50%;
    background: var(--brand-green);
  }
  .brand-name {
    color: var(--white);
    font-weight: 500;
    font-size: 64px;
    line-height: 72px;
    letter-spacing: -1px;
    white-space: nowrap;
  }
  .opening-dates {
    position: absolute;
    left: 620px;
    top: 206px;
    color: var(--brand-green);
    font-weight: 600;
    font-size: 19px;
    line-height: 24px;
    white-space: nowrap;
  }
  .location {
    position: absolute;
    left: 620px;
    top: 266px;
    display: flex;
    align-items: center;
    gap: 9px;
    color: var(--white);
    font-weight: 500;
    font-size: 19px;
    line-height: 24px;
    white-space: nowrap;
  }
  .location-pin { width: 17px; height: 22px; }
</style>
</head>
<body>
  <main class="billboard">
    <div class="foliage foliage--left" role="img" aria-label="Photograph of green cannabis leaves"></div>
    <div class="foliage foliage--right" role="img" aria-label="Photograph of green cannabis leaves"></div>

    <section class="headline-banner">
      <h1 class="headline">EXPERIENCE<br>NATURE’S GIFT</h1>
      <p class="subline">REED &amp; VALE CANNABIS STORE</p>
    </section>

    <div class="brand">
      <span class="brand-dot"></span>
      <span class="brand-name">Reed &amp; Vale</span>
    </div>

    <p class="opening-dates">Open Aug 1 &middot; Grand Opening Aug 15</p>

    <p class="location">
      <svg class="location-pin" viewBox="0 0 17 22" aria-hidden="true">
        <path d="M8.5 0C3.8 0 0 3.7 0 8.3 0 14 8.5 22 8.5 22S17 14 17 8.3C17 3.7 13.2 0 8.5 0z" fill="var(--brand-green)"/>
        <circle cx="8.5" cy="8.3" r="3.2" fill="var(--board-dark)"/>
      </svg>
      off exit 4b maple grove rd
    </p>
  </main>
</body>
</html>
```